Modern Website Design for an Online Travel Agency.. Design Only!!

Hi there!

We are building an website for our travel agency that caters to tourists traveling to the Cayman Islands. We provide travel information and take bookings for various tours available here.

We need designs for 8 different web page layouts. You can see the layout specifications in two attached documents. We do not have a need for the coding to be done. This will simply act as a blueprint for our developer to build from.

The important pages are the 'Home Page' 'checkout page' and the ‘Checkout Page’ (Page 1 & 10 in the PDF ‘Website Layout’)

The MOST important page is ‘Tour Search Page’ (page 6)

If you intend on only submitting one page design, please submit a design for page 6. Be aware though, the more of these 3 page designs you submit, the more likely we are to move forward with you!

At this stage, we are simply looking to develop the most aesthetic website design layout possible.

- The website should be colour coordinated with the logo. You can most certainly use other colours if you feel they complement the overall design of the website well.

- Everything must be laid out in an EXTREMELY simple & ‘easy to navigate’ way. The key is simplicity & Functionality. There is no need for messy or elaborate graphics.

- The website MUST have a VERY clean and modern appearance.

- We want the main background to be white, but you can use light grey in places to compliment or add dimension if you feel necessary.

- We will appreciate a good use of shadows and especially a good use of icons. (You can see examples of icons we have already designed, we are definitely open to new icon design concepts too)

- We will reward imagination and original thinking! Essentially we want a website with a creative touch and unique design elements, whilst maintaining that clean and simple layout.

- Most importantly!! - Paying attention to the small details will be highly rewarded (A well balanced and seamless use of fonts, colours, dimensions, shadowing, positioning, etc)

If you have any questions, please don’t hesitate to ask.

We’re excited to see your design submissions!

Thank you!!

You can find all the support documents and content at: https://www.filevorra.net/sh/9qm2rtwplexan7c/QQBmTtZnPdLsWEGxvvaJpLmRw?dl=0

Target Market(s)

Tourists

Industry/Entity Type

Travel

Number of Pages Required

5+ page

Font styles to use
Sans Serif

Colors

Designer to choose colors to be used in the design.

Requirements
Must have
• Must be very clean and modern.
• Must be simple and bold
• Must be color coordinated in a way that makes sense
• White background
Nice to have
• Good use of shadows and Icons
Should not have
• Over use of messy graphics
• And design layout which is not right angled (using anything but vertical or horizontal for the edges in the design)

```html
<!DOCTYPE html>
<html lang="en">
<head>
<meta charset="utf-8">
<title>TripIsle – Tour Search</title>
<link href="https://fonts.googleapis.com/css2?family=Jost:wght@400;500;600;700&family=Montserrat:wght@400;500;600&display=swap" rel="stylesheet">
<style>
:root{
  --blue:#0b5fe8;
  --blue-dark:#0a47b8;
  --green:#8fd62f;
  --ink:#1f2a37;
  --muted:#6b7684;
  --line:#d9dee5;
  --panel:#eef1f5;
  --foot:#f5f6f8;
  --white:#ffffff;
  --star:#f6b21b;
}
*{box-sizing:border-box;margin:0;padding:0}
html,body{width:1200px;height:2265px;overflow:hidden;background:var(--white)}
body{font-family:"Montserrat",sans-serif;color:var(--ink);position:relative}
.abs{position:absolute}

/* header */
.site-header{position:absolute;left:0;top:0;width:1200px;height:93px;background:var(--white)}
.brand{position:absolute;left:160px;top:26px;display:flex;align-items:center;gap:10px;font-family:"Jost",sans-serif;font-weight:600;font-size:30px;color:var(--blue)}
.brand-mark{width:34px;height:34px;background:var(--green);border-radius:4px}
.socials{position:absolute;left:545px;top:36px;display:flex;gap:19px}
.social{width:20px;height:20px;border:2px solid var(--blue);border-radius:5px}
.top-link{position:absolute;top:38px;font-size:15px;font-weight:500;color:var(--ink)}
.login{position:absolute;left:912px;top:26px;width:125px;height:41px;border:1.5px solid var(--blue);color:var(--blue);font-weight:600;font-size:17px;display:flex;align-items:center;justify-content:center;letter-spacing:.5px}

/* hero */
.hero{position:absolute;left:0;top:93px;width:1200px;height:575px;background:linear-gradient(180deg,#1e7fe0 0%,#3ea3ee 40%,#2bc3c9 58%,#16b3b0 75%,#0e9a98 100%)}
.main-nav{position:absolute;top:20px;left:0;width:1200px;display:flex;justify-content:center;gap:32px;color:var(--white);font-size:15px;font-weight:500}
.hero h1{position:absolute;left:160px;top:148px;font-family:"Jost",sans-serif;font-weight:700;font-size:52px;color:var(--white);letter-spacing:.5px}
.hero .sub{position:absolute;left:160px;top:217px;font-family:"Jost",sans-serif;font-size:33px;color:var(--white)}
.hero-search{position:absolute;left:165px;top:282px;height:51px;display:flex;background:var(--white)}
.hs-field{width:229px;display:flex;align-items:center;gap:10px;padding-left:28px;border-right:1px solid var(--line)}
.hs-field b{display:block;font-weight:500;font-size:11px}
.hs-field small{display:block;font-size:8px;color:var(--muted)}
.hs-btn{width:106px;background:var(--blue);color:var(--white);font-size:11px;font-weight:600;display:flex;align-items:center;justify-content:center;gap:8px}
.hero .help{position:absolute;left:162px;top:358px;color:var(--white);font-family:"Jost",sans-serif;font-size:20px}
.near{position:absolute;left:163px;top:398px;width:179px;height:23px;background:var(--white);color:var(--blue);font-size:11px;display:flex;align-items:center;gap:10px;padding-left:17px}
.near i{width:12px;height:12px;border-radius:50%;border:3px solid var(--blue)}

/* search row */
.map{position:absolute;left:160px;top:724px;width:282px;height:125px;border:1px solid var(--line);background:linear-gradient(135deg,#cfe3f3,#b8d5ec 60%,#dbe8c9)}
.search-panel{position:absolute;left:452px;top:724px;width:587px;height:125px;background:var(--panel);border:1px solid var(--line)}
.sp-input{position:absolute;left:13px;top:33px;width:278px;height:58px;background:var(--white);border:1px solid var(--line);display:flex;align-items:center;gap:10px;padding-left:18px;font-size:11px;color:var(--muted)}
.sp-btn{position:absolute;left:291px;top:33px;width:65px;height:58px;background:var(--blue);display:flex;align-items:center;justify-content:center}
.sort-label{position:absolute;left:388px;top:54px;font-size:12px;color:var(--muted)}
.sort{position:absolute;left:450px;top:46px;width:124px;height:32px;background:var(--white);border:1px solid var(--line);font-size:12px;color:#999;padding:7px 16px}

/* filters */
.filters{position:absolute;left:160px;top:869px;width:282px;height:776px;border:1px solid var(--line);background:var(--white)}
.f-head{height:39px;background:var(--panel);display:flex;justify-content:space-between;align-items:center;padding:0 14px;font-size:12px;color:var(--muted)}
.f-title{position:absolute;left:12px;font-size:11px;font-weight:600}
.f-text{position:absolute;left:12px;font-size:11px;color:#444;line-height:18px}
.chev{position:absolute;right:12px;width:6px;height:6px;border-right:1px solid #777;border-bottom:1px solid #777;transform:rotate(45deg)}
.slider{position:absolute;left:30px;width:226px;height:2px;background:var(--blue)}
.slider::before,.slider::after{content:"";position:absolute;top:-5px;width:11px;height:11px;border-radius:50%;border:1px solid #aaa;background:var(--white)}
.slider::before{left:-5px}.slider::after{right:-5px}
.range{position:absolute;left:24px;width:238px;display:flex;justify-content:space-between;font-size:8px;color:#555}
.icons{position:absolute;left:12px;top:463px;display:flex;gap:16px}
.icons span{width:29px;height:29px;border-radius:50%;background:var(--panel);display:flex;align-items:center;justify-content:center}
.check{position:absolute;left:15px;display:flex;align-items:center;gap:14px;font-size:11px;color:#444}
.check i{width:15px;height:15px;border:1px solid #bbb}

/* cards */
.card{position:absolute;width:271px;height:373px;border:1px solid var(--line);background:var(--white)}
.card .photo{height:207px;position:relative}
.tag{position:absolute;left:0;top:0;min-width:110px;height:23px;background:var(--green);color:var(--blue);font-size:11px;padding:4px 12px 0 18px;white-space:nowrap}
.price{position:absolute;right:0;bottom:0;width:135px;height:24px;background:var(--blue);color:var(--white);font-size:7px;display:flex;align-items:center;justify-content:center;gap:3px}
.price b{font-size:13px;font-weight:500;color:#d8f27a}
.card h3{position:absolute;left:14px;top:224px;font-family:"Jost",sans-serif;font-weight:500;font-size:15px}
.stars{position:absolute;left:14px;top:249px;font-size:8px;color:var(--star);letter-spacing:3px}
.stars em{font-style:normal;color:#555;letter-spacing:0;margin-left:6px;font-size:7px}
.loc{position:absolute;left:14px;top:270px;font-size:10px}
.dur{position:absolute;left:14px;top:290px;font-size:6px;color:#666}
.org{position:absolute;left:0;bottom:0;width:100%;height:56px;background:#f3f5f8;display:flex;align-items:center;gap:12px;padding-left:14px;font-size:11px}
.org i{width:35px;height:35px;border-radius:50%;background:var(--white);border:1px solid var(--line);display:flex;align-items:center;justify-content:center}
.org i b{width:14px;height:14px;background:var(--green);border-radius:2px}

/* promo */
.promo{position:absolute;top:1710px;width:416px;height:223px;background:var(--white);box-shadow:0 2px 14px rgba(0,0,0,.1);overflow:hidden}
.num{position:absolute;left:22px;top:24px;width:45px;height:42px;border-radius:50%;background:#e6eef8;color:var(--blue);font-family:"Jost",sans-serif;font-size:22px;display:flex;align-items:center;justify-content:center}
.promo h2{position:absolute;left:29px;top:79px;font-family:"Jost",sans-serif;font-weight:400;font-size:20px;line-height:19px;color:var(--blue)}
.promo p{position:absolute;left:29px;font-size:7px;line-height:8.5px;color:#333;width:190px}
.btn{position:absolute;height:15px;font-size:5.5px;color:var(--white);display:flex;align-items:center;justify-content:center}
.btn.g{background:#7ec81f}.btn.b{background:var(--blue)}
.art{position:absolute;border-radius:4px}
.arrow{position:absolute;top:1806px;width:32px;height:32px;border-radius:50%;border:1px solid #bbb;background:var(--white);display:flex;align-items:center;justify-content:center}

/* footer */
.footer{position:absolute;left:0;top:1970px;width:1200px;height:255px;background:var(--foot);border-top:1px solid #e8eaee;border-bottom:1px solid #e8eaee}
.fcol{position:absolute;font-size:11px;color:#555;line-height:22.5px}
.fcol h4{font-size:11px;font-weight:600;color:var(--ink)}
.fsoc{display:flex;gap:8px;margin-top:8px}
.fsoc i{width:18px;height:18px;border:1.5px solid #555;border-radius:4px}
.copy{position:absolute;top:2237px;width:1200px;text-align:center;font-size:10px;color:#888}
</style>
</head>
<body>

<header class="site-header">
  <div class="brand"><span class="brand-mark"></span>TripIsle</div>
  <div class="socials"><span class="social"></span><span class="social"></span><span class="social"></span><span class="social"></span></div>
  <div class="top-link" style="left:722px">Destinations ⌄</div>
  <div class="top-link" style="left:850px">USD$</div>
  <div class="login">LOG IN</div>
</header>

<section class="hero" role="img" aria-label="Turquoise sea with palm-lined beach and villas under a blue sky">
  <nav class="main-nav"><span>Discover Cayman</span><span>Thing to Do</span><span>My Trip Planner</span><span>Map</span><span>Contact Us</span></nav>
  <h1>LIVE EPIC MOMENTS</h1>
  <div class="sub">Book 7710 adventure activities worldwide</div>
  <div class="hero-search">
    <div class="hs-field">
      <svg width="18" height="20" viewBox="0 0 18 20"><path d="M9 1a6 6 0 0 1 6 6c0 5-6 11-6 11S3 12 3 7a6 6 0 0 1 6-6z" fill="none" stroke="#333" stroke-width="1.2"/><circle cx="9" cy="7" r="2" fill="none" stroke="#333"/></svg>
      <div><b>Your destination</b><small>Country,regiopn,city...</small></div>
    </div>
    <div class="hs-field" style="width:232px;border-right:0;position:relative">
      <svg width="20" height="20" viewBox="0 0 20 20"><circle cx="12" cy="3" r="2" fill="none" stroke="#333"/><path d="M11 6l-3 6 4 2-2 5M8 9l-4 1M11 8l4 3M8 12l-4 5" fill="none" stroke="#333" stroke-width="1.2"/></svg>
      <div><b>Our activities</b><small>ALL</small></div>
      <span class="chev" style="right:48px;top:20px"></span>
    </div>
    <div class="hs-btn">
      <svg width="20" height="20" viewBox="0 0 20 20"><circle cx="8" cy="8" r="6" fill="none" stroke="#fff" stroke-width="1.6"/><path d="M12.5 12.5l6 6" stroke="#fff" stroke-width="2"/></svg>SEARCH
    </div>
  </div>
  <div class="help">Find live-track easy to help ___</div>
  <div class="near"><i></i>Find activities near me</div>
</section>

<div class="map" role="img" aria-label="Map of the Caribbean with a pin on the Cayman Islands"></div>
<div class="search-panel">
  <div class="sp-input">
    <svg width="14" height="16" viewBox="0 0 18 20"><path d="M9 1a6 6 0 0 1 6 6c0 5-6 11-6 11S3 12 3 7a6 6 0 0 1 6-6z" fill="none" stroke="#555" stroke-width="1.4"/><circle cx="9" cy="7" r="2" fill="none" stroke="#555"/></svg>
    Your destination...
  </div>
  <div class="sp-btn"><svg width="30" height="30" viewBox="0 0 20 20"><circle cx="8" cy="8" r="6" fill="none" stroke="#fff" stroke-width="1.3"/><path d="M12.5 12.5l6 6" stroke="#fff" stroke-width="1.8"/></svg></div>
  <div class="sort-label">Sort by:</div>
  <div class="sort">poulalarity<span class="chev" style="top:11px;right:12px"></span></div>
</div>

<aside class="filters">
  <div class="f-head"><span>⫶ FILTERS</span><span>Reset filters</span></div>
  <div class="f-title" style="top:64px">Location</div>
  <div class="f-text" style="top:81px">- Grand Cayman<br>- Cayman Brac</div>
  <div class="f-title" style="top:133px">Pricing Range</div><span class="chev" style="top:134px"></span>
  <div class="slider" style="top:168px"></div>
  <div class="range" style="top:185px"><span>□1,005</span><span>□1,1005</span></div>
  <div class="f-title" style="top:223px">Duration</div><span class="chev" style="top:224px"></span>
  <div class="slider" style="top:258px"></div>
  <div class="range" style="top:275px"><span>□1,005 km</span><span>□1,1005 km</span></div>
  <div class="f-title" style="top:313px">People in your Group</div><span class="chev" style="top:314px"></span>
  <div class="slider" style="top:348px"></div>
  <div class="range" style="top:365px"><span>□0 hours</span><span>□7days</span></div>
  <div class="abs" style="left:16px;top:393px;width:250px;height:1px;background:var(--line)"></div>
  <div class="f-title" style="top:431px">Activities</div>
  <div class="icons">
    <span><svg width="14" height="14" viewBox="0 0 14 14"><path d="M1 5L7 1l6 4zM2 6h10v1H2zM3 8h1v4H3zM6 8h1v4H6zM9 8h1v4H9zM1 12h12v1H1z" fill="#0b5fe8"/></svg></span>
    <span><svg width="14" height="14" viewBox="0 0 14 14"><rect x="1" y="4" width="12" height="6" rx="1" fill="#0b5fe8"/><circle cx="4" cy="11" r="1.3" fill="#0b5fe8"/><circle cx="10" cy="11" r="1.3" fill="#0b5fe8"/></svg></span>
    <span><svg width="14" height="14" viewBox="0 0 14 14"><path d="M1 8h12l-2-2H7L4 3H3l1 3H1z" fill="#0b5fe8"/></svg></span>
    <span><svg width="14" height="14" viewBox="0 0 14 14"><path d="M1 10q6-8 12 0zM1 12h12" fill="#0b5fe8" stroke="#0b5fe8"/></svg></span>
    <span><svg width="14" height="14" viewBox="0 0 14 14"><path d="M7 1l6 12H1z" fill="#0b5fe8"/></svg></span>
  </div>
  <div class="check" style="top:512px"><i></i>Kiteboarding</div>
  <div class="check" style="top:534px"><i></i>Museums</div>
  <div class="check" style="top:557px"><i></i>Boat Trips</div>
  <div class="check" style="top:579px"><i></i>Others</div>
  <div class="f-title" style="top:625px">Other Filters</div>
  <div class="check" style="top:654px"><i></i>Fitness Level</div>
  <div class="check" style="top:677px"><i></i>Museums</div>
  <div class="check" style="top:699px"><i></i>Others</div>
</aside>

<article class="card" style="left:475px;top:870px">
  <div class="photo" role="img" aria-label="Group riding horses along a sandy beach" style="background:linear-gradient(180deg,#8fc4e6,#6fb6c9 40%,#d8cdb6 70%,#b9a88c)">
    <div class="tag">Beach Ride</div>
    <div class="price">From □ <b>$445/</b> Per person</div>
  </div>
  <h3>Beach Ride</h3>
  <div class="stars">★★★★★<em>reviews</em></div>
  <div class="loc">⚲ Location Cayman</div>
  <div class="dur">◷ 22 hrs</div>
  <div class="org"><i><b></b></i>Organized by: TripIsle</div>
</article>

<article class="card" style="left:766px;top:870px">
  <div class="photo" role="img" aria-label="Swimmer in a life vest with a dolphin in turquoise water" style="background:linear-gradient(160deg,#4fc4d8,#2aa6c4 50%,#1b7fa2)">
    <div class="tag">Dolphin Lagoon</div>
    <div class="price">From □ <b>$445/</b> Per person</div>
  </div>
  <h3>Lagoon Dolphin Swim</h3>
  <div class="stars">★★★★★<em>reviews</em></div>
  <div class="loc">⚲ Location Cayman</div>
  <div class="dur">◷ 22 hrs</div>
  <div class="org"><i><b></b></i>Organized by: TripIsle</div>
</article>

<article class="card" style="left:473px;top:1275px">
  <div class="photo" role="img" aria-label="Gallery interior with framed works and a wooden boat on display" style="background:linear-gradient(180deg,#3a3a3c,#8e8a82 50%,#c9c2b5)">
    <div class="tag">Island Gallery</div>
    <div class="price">From □ <b>$445/</b> Per person</div>
  </div>
  <h3>Island Art Gallery</h3>
  <div class="stars">★★★★★<em>reviews</em></div>
  <div class="loc">⚲ Location Cayman</div>
  <div class="dur">◷ 22 hrs</div>
  <div class="org"><i><b></b></i>Organized by: TripIsle</div>
</article>

<article class="card" style="left:766px;top:1275px">
  <div class="photo" role="img" aria-label="Cave with stalactites reflected in a clear pool" style="background:linear-gradient(180deg,#4a3a2c,#8a6f52 45%,#2f6f86 80%,#14384a)">
    <div class="tag">grotto</div>
    <div class="price">From □ <b>$445/</b> Per person</div>
  </div>
  <h3>Grotto caves</h3>
  <div class="stars">★★★★★<em>reviews</em></div>
  <div class="loc">⚲ Location Cayman</div>
  <div class="dur">◷ 22 hrs</div>
  <div class="org"><i><b></b></i>Organized by: TripIsle</div>
</article>

<div class="arrow" style="left:133px"><svg width="16" height="10" viewBox="0 0 16 10"><path d="M15 5H1M5 1L1 5l4 4" fill="none" stroke="#333" stroke-width="1.3"/></svg></div>
<div class="arrow" style="left:1035px"><svg width="16" height="10" viewBox="0 0 16 10"><path d="M1 5h14M11 1l4 4-4 4" fill="none" stroke="#333" stroke-width="1.3"/></svg></div>

<section class="promo" style="left:171px">
  <div class="num">1.</div>
  <h2>Choose Your<br>Favorite Activities</h2>
  <p style="top:134px">Discover everything you need to know about travel &amp; safety in the Cayman Islands and browse every fun activity available here.</p>
  <div class="btn g" style="left:29px;top:176px;width:61px">Learn About Cayman</div>
  <div class="btn b" style="left:96px;top:176px;width:62px">Find Things To Do</div>
  <div class="art" role="img" aria-label="Illustration of a relaxed traveller surrounded by activity icons" style="left:236px;top:22px;width:166px;height:180px;background:radial-gradient(circle at 50% 50%,#e3f5c6,#eef4fb 70%,#fff)"></div>
</section>

<section class="promo" style="left:611px">
  <div class="num">2.</div>
  <h2>Use Our Online<br>Travel Planner</h2>
  <p style="top:128px">Organize your favorite activities on our user-friendly trip planner to effortlessly design your perfect vacation. Use our planner to easily budget your entire trip!</p>
  <div class="btn g" style="left:28px;top:170px;width:61px">Go To Trip Planner</div>
  <div class="btn b" style="left:95px;top:170px;width:61px">View video</div>
  <div class="art" role="img" aria-label="Illustration of a traveller planning a trip on a large screen with luggage" style="left:236px;top:22px;width:166px;height:180px;background:radial-gradient(circle at 50% 50%,#e3f5c6,#e8f1fb 70%,#fff)"></div>
</section>

<footer class="footer">
  <div class="fcol" style="left:240px;top:84px"><h4>Company</h4>About us<br>How it works ?<br>Our investors<br>Contact us<br>Work with us</div>
  <div class="fcol" style="left:448px;top:91px"><h4>Support</h4>FAQ<br>Legal notices<br>Cancellation policy<br>Terms of use<br>Privacy policy</div>
  <div class="fcol" style="left:663px;top:94px"><h4>Follow us</h4>Press room<br>Our ambassadors<br>Magazine<div class="fsoc"><i></i><i></i><i></i><i></i></div></div>
  <div class="fcol" style="left:883px;top:91px"><h4>Partners</h4>Offer your activities<br>Become an affiliate</div>
</footer>
<div class="copy">Copyright 2019</div>

</body>
</html>
```